Harbour Lantern Fliers and logo design

We need to design a product logo and some informational fliers for a summit quest.
I have attached our Harbour Lantern logo - colours need to be complimentary but not the same, we would like fresh, funky but still professional. We generally communicate in a fairly casual way to reach our market. (We don't like boring)
Clear and simple - not too busy
images are good but not actual photos
Here is our website to give you an idea www.harbourlantern-example.co.nz
The flier is a 3 page document.
The logo is to say Summit Quest. The challenge is based on exercise, connecting with people, giving, learning and taking notice (The 4 keys to brightwater) Once agin the logo needs to be complementary but not the same.
The Harbour lantern logo needs to be on the fliers but the summit quest logo is separate.
Thanks very much!!

```html
<!DOCTYPE html>
<html lang="en">
<head>
<meta charset="utf-8">
<title>Stress Buster – Harbour Lantern</title>
<link href="https://fonts.googleapis.com/css2?family=Open+Sans:ital,wght@0,400;0,600;0,700;1,700&family=Fjalla+One&display=swap" rel="stylesheet">
<style>
  :root {
    --lime: #9cc43f;
    --lime-pale: #cfe496;
    --green-dark: #6e9e2a;
    --heading-green: #7fb033;
    --teal: #2fa79b;
    --red: #e2413a;
    --text: #3c3c3c;
    --paper: #ffffff;
  }
  * { box-sizing: border-box; margin: 0; padding: 0; }
  html, body { width: 900px; height: 1200px; overflow: hidden; background: var(--paper); }
  body { font-family: "Open Sans", Arial, sans-serif; color: var(--text); position: relative; }

  .side-band { position: absolute; left: 0; top: 0; width: 230px; height: 1200px; }
  .side-title {
    position: absolute; left: 30px; top: 110px; height: 1050px; width: 170px;
    writing-mode: vertical-rl; transform: rotate(180deg);
    font-family: "Fjalla One", Impact, sans-serif; font-size: 150px; line-height: 170px;
    color: var(--lime-pale); -webkit-text-stroke: 2px var(--paper);
    text-align: center; letter-spacing: 2px;
  }

  .brand { position: absolute; right: 50px; top: 40px; display: flex; align-items: center; gap: 14px; }
  .brand-dot { width: 34px; height: 34px; border-radius: 50%; background: var(--lime); }
  .brand-name { font-size: 38px; font-weight: 700; color: var(--green-dark); line-height: 1; }

  .content { position: absolute; left: 272px; top: 130px; width: 590px; }
  .lead {
    font-style: italic; font-weight: 700; font-size: 25px; line-height: 1.25;
    color: var(--heading-green); text-align: center; margin-bottom: 26px;
  }
  .intro p { font-size: 15px; line-height: 1.45; margin-bottom: 14px; }

  .steps { display: grid; grid-template-columns: 1fr 1fr; column-gap: 40px; row-gap: 24px; margin-top: 22px; }
  .step-head { display: flex; align-items: center; gap: 12px; margin-bottom: 10px; }
  .step-letter {
    width: 40px; height: 40px; border-radius: 50%; color: #fff; font-weight: 700; font-size: 20px;
    display: flex; align-items: center; justify-content: center;
  }
  .step-name {
    height: 34px; padding: 0 20px; display: flex; align-items: center;
    font-weight: 600; font-size: 16px; color: #fff; border-radius: 0 17px 17px 0; margin-left: -22px; padding-left: 28px;
    flex: 1;
  }
  .step--stop .step-letter, .step--stop .step-name { background: var(--red); }
  .step--take .step-letter, .step--take .step-name { background: var(--teal); }
  .step--observe .step-letter, .step--observe .step-name { background: var(--lime); }
  .step--proceed .step-letter, .step--proceed .step-name { background: var(--green-dark); }
  .step p { font-size: 15px; line-height: 1.45; margin-bottom: 8px; }
  .step h4 { font-size: 15px; color: var(--heading-green); font-weight: 700; margin-top: 6px; }

  .stop-reminder { display: flex; align-items: center; gap: 16px; margin-top: 26px; }
  .stop-list { font-size: 17px; line-height: 1.3; color: var(--red); font-variant: small-caps; font-weight: 600; }
</style>
</head>
<body>
  <svg class="side-band" viewBox="0 0 230 1200" aria-hidden="true">
    <path d="M0 0 H185 Q230 0 230 45 V1200 H0 Z" fill="var(--lime)"/>
  </svg>
  <div class="side-title">Stress Buster!</div>

  <div class="brand">
    <span class="brand-dot"></span>
    <span class="brand-name">harbour lantern</span>
  </div>

  <main class="content">
    <p class="lead">We cannot control what happens to us in life,<br>but we can change the way we react</p>

    <section class="intro">
      <p>Stress happens because we are allowing fear, anger, disappointment and a host of other negative emotions to navigate our actions. By becoming aware of these emotions and allowing them to simply be, we can begin to gain control of how we react and respond to stressful situations.</p>
      <p>Our experience is always changing. Without awareness, mental patterns related to what we fear and what upsets us make life harder.</p>
      <p>S.T.O.P is a powerful, yet surprisingly basic strategy that helps you to be focused, alert, relaxed and at your emotional best when stressful moments present themselves in your life.</p>
      <p>Simply put, it's a four-step checklist to use anytime you want to ground yourself and get some insight into whatever is going on. The whole idea behind it is that by taking a very brief break—even less than one minute—you can determine the very best action to take in the moment.</p>
    </section>

    <section class="steps">
      <div class="step step--stop">
        <div class="step-head"><span class="step-letter">S</span><span class="step-name">Stop</span></div>
        <p>Stop what you are doing. Press the pause button on your thoughts and actions.</p>
      </div>
      <div class="step step--take">
        <div class="step-head"><span class="step-letter">T</span><span class="step-name">Take</span></div>
        <p>Take a few deep breaths to centre yourself and bring yourself fully into the present moment.</p>
      </div>
      <div class="step step--observe">
        <div class="step-head"><span class="step-letter">O</span><span class="step-name">Observe</span></div>
        <p>Observe what is going on with your:</p>
        <h4>Body</h4>
        <p>What physical sensations are you aware of (touch, sight, hearing, taste, smell)?</p>
        <h4>Emotions</h4>
        <p>What are you feeling right now?</p>
        <h4>Mind</h4>
        <p>What assumptions are you making about your feelings? What is the story you're telling yourself about why you are having them?</p>
      </div>
      <div class="step step--proceed">
        <div class="step-head"><span class="step-letter">P</span><span class="step-name">Proceed</span></div>
        <p>Proceed with whatever you were doing, making a conscious, intentional choice to incorporate what you just learned.</p>
        <div class="stop-reminder">
          <svg width="92" height="92" viewBox="0 0 100 100" role="img" aria-label="Stop sign">
            <polygon points="30,2 70,2 98,30 98,70 70,98 30,98 2,70 2,30" fill="var(--red)" stroke="#fff" stroke-width="4"/>
            <polygon points="31,8 69,8 92,31 92,69 69,92 31,92 8,69 8,31" fill="none" stroke="#fff" stroke-width="2"/>
            <text x="50" y="59" text-anchor="middle" font-family="Open Sans, Arial, sans-serif" font-weight="700" font-size="26" fill="#fff">STOP</text>
          </svg>
          <div class="stop-list">Stop<br>Take a breath<br>Observe<br>Proceed</div>
        </div>
      </div>
    </section>
  </main>
</body>
</html>
```